Business Card Design Project

We are a construction company in Orange County, CA. We need a two sided business card. We would like the back to be our logo with web URL. Front should included Name, title, address, phone, fax and email address.

our address is
387 West Marlowe Blvd, Suite 402
Larkhaven, CA 90000

Our logo files are attached.

Construction

```html
<!DOCTYPE html>
<html lang="en">
<head>
<meta charset="utf-8">
<title>Brelva Business Card – Front and Back</title>
<link rel="stylesheet" href="https://fonts.googleapis.com/css2?family=Roboto+Condensed:ital,wght@0,700;1,700&family=Open+Sans:ital,wght@1,700&display=swap">
<style>
  :root {
    --brand-blue: #1b4b80;
    --ink: #111111;
    --ghost: #e3e4eb;
    --card-white: #ffffff;
    --card-dark: #252525;
    --url-grey: #3b3b3b;
    --page: #ffffff;
    --card-edge: #c9c9c9;
  }
  * { margin: 0; padding: 0; box-sizing: border-box; }
  html, body { width: 1200px; height: 1000px; overflow: hidden; background: var(--page); }
  .sheet { position: relative; width: 1200px; height: 1000px; }

  .card {
    position: absolute;
    left: 228px;
    width: 744px;
    height: 432px;
    overflow: hidden;
    box-shadow: 2px 3px 4px rgba(0,0,0,0.25);
  }
  .card-front { top: 53px; background: var(--card-white); border: 1px solid var(--card-edge); }
  .card-back { top: 517px; background: var(--card-dark); }

  .front-watermark {
    position: absolute;
    left: 4px;
    top: 17px;
    font-family: "Roboto Condensed", sans-serif;
    font-weight: 700;
    font-size: 330px;
    line-height: 1;
    color: var(--ghost);
    white-space: nowrap;
    letter-spacing: -4px;
  }

  .contact {
    position: absolute;
    right: 30px;
    top: 52px;
    text-align: right;
    font-family: "Roboto Condensed", sans-serif;
    font-weight: 700;
  }
  .contact-name { font-size: 40px; line-height: 44px; color: var(--brand-blue); }
  .contact-title { font-size: 28px; line-height: 32px; color: var(--ink); }
  .contact-email { margin-top: 26px; font-size: 30px; line-height: 34px; color: var(--brand-blue); }
  .contact-phones { margin-top: 30px; font-family: "Open Sans", sans-serif; font-style: italic; font-weight: 700; font-size: 23px; line-height: 30px; }
  .phone-label { color: var(--ink); display: inline-block; width: 56px; text-align: left; }
  .phone-number { color: var(--brand-blue); }

  .address {
    position: absolute;
    left: 28px;
    top: 308px;
    font-family: "Open Sans", sans-serif;
    font-style: italic;
    font-weight: 700;
    font-size: 17px;
    line-height: 24px;
    color: var(--ink);
  }

  .front-wordmark {
    position: absolute;
    right: 30px;
    top: 320px;
    font-family: "Roboto Condensed", sans-serif;
    font-weight: 700;
    font-size: 80px;
    line-height: 1;
    color: var(--brand-blue);
  }

  .back-lockup {
    position: absolute;
    left: 0;
    right: 0;
    top: 118px;
    text-align: center;
    font-family: "Roboto Condensed", sans-serif;
    font-weight: 700;
  }
  .back-wordmark { font-size: 160px; line-height: 160px; color: var(--brand-blue); }
  .back-url { margin-top: 24px; font-size: 40px; line-height: 44px; color: var(--url-grey); }
</style>
</head>
<body>
<main class="sheet">
  <section class="card card-front" aria-label="Card front">
    <div class="front-watermark" aria-hidden="true">BRELVA</div>

    <div class="contact">
      <p class="contact-name">Daniel Rourke</p>
      <p class="contact-title">JOB TITLE</p>
      <p class="contact-email">drourke@brelvacs.com</p>
      <div class="contact-phones">
        <p><span class="phone-label">Tel:</span> <span class="phone-number">(555) 014-2207</span></p>
        <p><span class="phone-label">Fax:</span> <span class="phone-number">(555) 014-2207</span></p>
      </div>
    </div>

    <address class="address">
      387 West Marlowe Blvd<br>
      Suite 402<br>
      Larkhaven<br>
      CA 90000
    </address>

    <div class="front-wordmark">BRELVA</div>
  </section>

  <section class="card card-back" aria-label="Card back">
    <div class="back-lockup">
      <p class="back-wordmark">BRELVA</p>
      <p class="back-url">www.brelvacs.com</p>
    </div>
  </section>
</main>
</body>
</html>
```